Blue Heron IT Business Card - Clean, Simple

Need a simple, clean standard sized business card for an IT consulting business using existing logo and company colours. Background should be mainly white. Feel free to be creative but clean, simple, quiet design is preferred. Font is specified in logo but any sans serif fonts work.

Contact Information for card is as follows (doesn't need to be in this exact order):

Malcolm Pettigrew
Owner
malcolm@blueheronit.ca
705-412-9083
www.blueheronit.ca

Target Market(s)

Small to medium sized business.

Industry/Entity Type

IT Consulting

Contact Information for Business Card

Logo and contact info.

Font styles to use
Sans Serif

Colors
EE7325
F08F49
F5BC92
FAE3D3
FDF4ED

Requirements
Must have
• All white or mostly white background.

```html
<!DOCTYPE html>
<html lang="en">
<head>
<meta charset="utf-8">
<title>Blue Heron IT – Business Card</title>
<link href="https://fonts.googleapis.com/css2?family=Montserrat:wght@400;500;700&display=swap" rel="stylesheet">
<style>
  :root {
    --orange: #EE7325;
    --orange-soft: #F08F49;
    --ink: #2b2b2d;
    --paper: #ffffff;
    --backdrop: #2a2a2c;
  }
  * { margin: 0; padding: 0; box-sizing: border-box; }
  html, body { width: 1200px; height: 801px; overflow: hidden; }
  body {
    background: var(--backdrop);
    font-family: "Montserrat", sans-serif;
    position: relative;
  }
  .card {
    position: absolute;
    width: 560px;
    height: 320px;
    background: var(--paper);
    border-radius: 16px;
    border-bottom: 3px solid var(--orange);
    box-shadow: 0 10px 24px rgba(0,0,0,.35);
  }
  .card-front { left: 60px; top: 70px; }
  .card-back  { left: 580px; top: 410px; }

  .brand {
    display: flex;
    align-items: center;
    gap: 14px;
  }
  .brand-dot {
    width: 34px; height: 34px;
    border-radius: 50%;
    background: var(--orange);
    flex: none;
  }
  .brand-name {
    font-weight: 700;
    font-size: 40px;
    color: var(--ink);
    letter-spacing: -0.5px;
    white-space: nowrap;
  }
  .card-front .brand {
    position: absolute;
    left: 50%; top: 50%;
    transform: translate(-50%, -50%);
  }
  .card-back .brand {
    position: absolute;
    left: 34px; top: 190px;
  }
  .card-back .brand-name { font-size: 30px; }
  .card-back .brand-dot { width: 26px; height: 26px; }

  .divider {
    position: absolute;
    left: 318px; top: 40px;
    width: 1px; height: 150px;
    background: var(--ink);
  }
  .contact {
    position: absolute;
    left: 340px; top: 44px;
    right: 16px;
  }
  .contact-name {
    font-weight: 700;
    font-size: 19px;
    color: var(--ink);
    white-space: nowrap;
  }
  .contact-role {
    font-weight: 400;
    font-size: 13px;
    color: var(--orange);
    margin: 4px 0 18px;
  }
  .contact-list { list-style: none; }
  .contact-item {
    display: flex;
    align-items: center;
    gap: 8px;
    font-size: 12px;
    color: var(--ink);
    margin-bottom: 8px;
    white-space: nowrap;
  }
  .contact-icon { width: 13px; height: 13px; flex: none; fill: var(--orange); }
</style>
</head>
<body>
  <section class="card card-front" aria-label="Card front">
    <div class="brand">
      <span class="brand-dot"></span>
      <span class="brand-name">Blue Heron IT</span>
    </div>
  </section>

  <section class="card card-back" aria-label="Card back">
    <div class="brand">
      <span class="brand-dot"></span>
      <span class="brand-name">Blue Heron IT</span>
    </div>
    <span class="divider"></span>
    <div class="contact">
      <p class="contact-name">Malcolm Pettigrew</p>
      <p class="contact-role">Owner</p>
      <ul class="contact-list">
        <li class="contact-item">
          <svg class="contact-icon" viewBox="0 0 24 24"><path d="M6.6 10.8a15.1 15.1 0 0 0 6.6 6.6l2.2-2.2a1 1 0 0 1 1-.25 11.4 11.4 0 0 0 3.6.57 1 1 0 0 1 1 1V20a1 1 0 0 1-1 1A17 17 0 0 1 3 4a1 1 0 0 1 1-1h3.5a1 1 0 0 1 1 1c0 1.25.2 2.45.57 3.57a1 1 0 0 1-.25 1z"/></svg>
          705-412-9083
        </li>
        <li class="contact-item">
          <svg class="contact-icon" viewBox="0 0 24 24"><path d="M2 5h20v14H2z M2 5l10 8 10-8" fill="none" stroke="var(--orange)" stroke-width="0"/><path d="M2 5h20v2l-10 7L2 7z"/><path d="M2 9l10 7 10-7v10H2z"/></svg>
          malcolm@blueheronit.ca
        </li>
        <li class="contact-item">
          <svg class="contact-icon" viewBox="0 0 24 24"><circle cx="12" cy="12" r="10"/><path d="M2 12h20M12 2c3 3 3 17 0 20M12 2c-3 3-3 17 0 20" stroke="#fff" stroke-width="1.4" fill="none"/></svg>
          www.blueheronit.ca
        </li>
      </ul>
    </div>
  </section>
</body>
</html>
```